New Business Card Design for Engineering and Surveying Company

We need a new design template for our business cards. We are a civil engineering, land surveying and pipeline integrity business. Please see brqholt.com for details. We need a bold, new business card design to complement our rebranding and marketing program. We have anew logo and attached vectro file. Please find additional details below. I am available to answer any questions.

Target Market(s)

Contractors, business owners, oil companies

Contact Information for Business Card

Needs to be customizable for different people (name, title, cell)

Font styles to use
Sans Serif
Other font styles liked:
• See eps file

Requirements
Must have
• Example Information:
Derek Fannaby

T:409-555-0187
M: 202-555-0143
dfannaby@brqholt.com

Address: 1870 Corvane Parkway, Beaumont, Texas 77701
Email: dfanbagy@brqholt.com
Website: www.brqholt.com
Nice to have
• I would like the back of the card to have the logo on a bold background with the text below:

[logo]
ROLAND FANNABY & ASSOCIATES
CIVIL ENGINEERING | LAND SURVEYING | PIPELINE INTEGRITY

The reverse side should have the contact information for the person (example above), a smaller version of the logo and a graphic

```html
<!DOCTYPE html>
<html lang="en">
<head>
<meta charset="utf-8">
<title>Roland Fannaby &amp; Associates — Business Card</title>
<link rel="stylesheet" href="https://fonts.googleapis.com/css2?family=Montserrat:wght@400;600;700;800&display=swap">
<style>
  :root {
    --page-bg: #8a8a8a;
    --card-white: #ffffff;
    --card-black: #000000;
    --brand-red: #e4202e;
    --brand-navy: #0b1420;
    --text-grey: #7a7a7a;
    --rule-grey: #9a9a9a;
  }
  * { margin: 0; padding: 0; box-sizing: border-box; }
  html, body {
    width: 1200px; height: 960px; overflow: hidden;
    background: var(--page-bg);
    font-family: "Montserrat", sans-serif;
  }
  .card {
    position: absolute;
    left: 281px;
    width: 655px; height: 374px;
    border-radius: 26px;
    overflow: hidden;
  }
  .card--front { top: 59px; background: var(--card-white); }
  .card--back  { top: 501px; background: var(--card-black); }

  .wordmark {
    position: absolute;
    display: flex; align-items: center; gap: 12px;
    font-weight: 800; letter-spacing: -1px; line-height: 1;
  }
  .wordmark__square { background: var(--brand-red); flex: none; }
  .card--front .wordmark { left: 54px; top: 150px; font-size: 66px; color: var(--brand-navy); }
  .card--front .wordmark__square { width: 34px; height: 34px; }

  .divider {
    position: absolute; left: 328px; top: 68px;
    width: 2px; height: 240px; background: var(--rule-grey);
  }
  .contact { position: absolute; left: 347px; top: 66px; color: var(--text-grey); }
  .contact__name {
    font-size: 26px; font-weight: 600; color: var(--brand-red); line-height: 28px;
  }
  .contact__title { font-size: 18px; line-height: 22px; margin-top: 0; }
  .contact__list { list-style: none; font-size: 17px; line-height: 22px; }
  .contact__list--direct { margin-top: 20px; }
  .contact__list--office { margin-top: 16px; }
  .contact__list li { display: flex; align-items: center; gap: 8px; }
  .contact__list svg { width: 14px; height: 14px; flex: none; fill: var(--brand-red); }
  .contact__address { font-size: 17px; line-height: 22px; margin-top: 16px; font-style: normal; }

  .card--back .wordmark {
    left: 0; right: 0; top: 110px; justify-content: center;
    font-size: 84px; color: var(--card-white); gap: 16px;
  }
  .card--back .wordmark__square { width: 44px; height: 44px; }
  .back__company {
    position: absolute; left: 0; right: 0; top: 274px; text-align: center;
    color: var(--brand-red); font-weight: 700; font-size: 17px;
  }
  .back__services {
    position: absolute; left: 0; right: 0; top: 300px; text-align: center;
    color: var(--card-white); font-weight: 400; font-size: 17px;
  }
</style>
</head>
<body>
  <section class="card card--front">
    <div class="wordmark"><span class="wordmark__square"></span>RFA</div>
    <div class="divider"></div>
    <div class="contact">
      <h1 class="contact__name">Derek Fannaby</h1>
      <p class="contact__title">Manager</p>
      <ul class="contact__list contact__list--direct">
        <li><svg viewBox="0 0 16 16"><path d="M3 1l3 3-2 2c1 2 4 5 6 6l2-2 3 3-2 2C7 15 1 9 1 3z"/></svg>409-555-0187</li>
        <li><svg viewBox="0 0 16 16"><path d="M4 0h8a1 1 0 0 1 1 1v14a1 1 0 0 1-1 1H4a1 1 0 0 1-1-1V1a1 1 0 0 1 1-1zm1 2v10h6V2zm3 11a1 1 0 1 0 0 2 1 1 0 0 0 0-2z"/></svg>202-555-0143</li>
        <li><svg viewBox="0 0 16 16"><path d="M1 4h14v9H1zm1 1l6 4 6-4z"/></svg>dfannaby@brqholt.com</li>
      </ul>
      <address class="contact__address">1870 Corvane Parkway<br>Beaumont, Texas 77701</address>
      <ul class="contact__list contact__list--office">
        <li><svg viewBox="0 0 16 16"><path d="M1 4h14v9H1zm1 1l6 4 6-4z"/></svg>dfanbagy@brqholt.com</li>
        <li><svg viewBox="0 0 16 16"><path d="M8 1a7 7 0 1 0 0 14A7 7 0 0 0 8 1zm0 1.5c.8 1 1.4 2.3 1.6 3.8H6.4C6.6 4.8 7.2 3.5 8 2.5zM2.6 7.3h2.7c0 .9.1 1.6.2 2.4H2.8a5.6 5.6 0 0 1-.2-2.4zm8.1 0h2.7c.1.8 0 1.6-.2 2.4h-2.7c.1-.8.2-1.5.2-2.4zm-4.3 0h3.2c0 .9-.1 1.7-.2 2.4H6.6c-.1-.7-.2-1.5-.2-2.4zM3.4 10.7h2.3c.3 1.2.7 2 1.2 2.8a5.6 5.6 0 0 1-3.5-2.8zm3.3 0h2.6c-.3 1.1-.7 2-1.3 2.8-.6-.8-1-1.7-1.3-2.8zm3.6 0h2.3a5.6 5.6 0 0 1-3.5 2.8c.5-.8.9-1.6 1.2-2.8zM3 6.3a5.6 5.6 0 0 1 3.8-3.7c-.6 1-1.1 2.3-1.4 3.7zm7.6 0c-.2-1.4-.7-2.7-1.4-3.7A5.6 5.6 0 0 1 13 6.3z"/></svg>www.brqholt.com</li>
      </ul>
    </div>
  </section>

  <section class="card card--back">
    <div class="wordmark"><span class="wordmark__square"></span>RFA</div>
    <p class="back__company">ROLAND FANNABY &amp; ASSOCIATES</p>
    <p class="back__services">CIVIL ENGINEERING | LAND SURVEYING | PIPELINE INTEGRITY</p>
  </section>
</body>
</html>
```